Home Security Company Business Card

Looking for a eye catching business card that is non traditional and stands out but yet still looks professional. It should include all the pertinent information such as name, title, address, telephone, e-mail, website address should definitely stand out and then finally the logo.

Target Market(s)

Residential and Commercial accounts mostly upscale accounts

Industry/Entity Type

Security

Contact Information for Business Card

Name
Title
Address
Office #
Cell #
E-mail
Website

Font styles to use
Serif
Sans Serif

Requirements
Must have
• Logo, two sided color configuration
Nice to have
• You decide
Should not have
• There really aren't any.

```html
<!DOCTYPE html>
<html lang="en">
<head>
<meta charset="utf-8">
<title>Ironvale Protection Group – Business Card</title>
<link rel="stylesheet" href="https://fonts.googleapis.com/css2?family=Open+Sans:wght@400;600;700&family=Tinos&display=swap">
<style>
  :root {
    --backdrop: #2a2c30;
    --crimson: #7d1616;
    --crimson-deep: #6a1212;
    --gold: #c98a1e;
    --gold-light: #e9b546;
    --paper: #ffffff;
    --ink: #1d1d1d;
    --rule: #bdbdbd;
  }
  * { box-sizing: border-box; margin: 0; padding: 0; }
  html, body {
    width: 1200px; height: 864px; overflow: hidden;
    background: var(--backdrop);
  }
  .canvas {
    width: 1200px; height: 864px;
    display: flex; align-items: center; justify-content: center; gap: 40px;
  }
  .card {
    width: 540px; height: 310px;
    position: relative;
    border-radius: 3px;
    box-shadow: 0 8px 24px rgba(0,0,0,.45);
    overflow: hidden;
  }
  .card--front {
    background: var(--crimson);
    display: flex; align-items: center; justify-content: center;
  }
  .brand { display: flex; align-items: center; gap: 14px; }
  .brand__mark {
    width: 74px; height: 74px; border-radius: 50%;
    background: var(--gold-light);
  }
  .brand__name {
    font-family: "Tinos", "Times New Roman", serif;
    font-size: 24px; line-height: 1.1; letter-spacing: .5px;
    text-transform: uppercase;
  }
  .card--front .brand__name { color: var(--paper); }

  .card--back { background: var(--paper); }
  .card--back .brand { position: absolute; top: 34px; right: 34px; gap: 10px; }
  .card--back .brand__mark { width: 50px; height: 50px; background: var(--gold); }
  .card--back .brand__name { color: var(--crimson); font-size: 17px; }

  .holder { position: absolute; left: 34px; top: 112px; font-family: "Open Sans", Arial, sans-serif; }
  .holder__name { color: var(--crimson); font-weight: 700; font-size: 22px; line-height: 1.1; }
  .holder__title { color: var(--gold); font-size: 13px; margin-top: 2px; }

  .divider {
    position: absolute; left: 150px; right: 34px; top: 164px;
    height: 1px; background: var(--rule);
  }

  .contact {
    position: absolute; right: 34px; top: 178px;
    list-style: none;
    font-family: "Open Sans", Arial, sans-serif; font-size: 14px; color: var(--ink);
    text-align: right;
  }
  .contact__item { display: flex; justify-content: flex-end; align-items: center; gap: 9px; height: 22px; }
  .contact__icon {
    width: 17px; height: 17px; background: var(--crimson-deep); border-radius: 2px;
    display: inline-flex; align-items: center; justify-content: center;
  }
  .contact__icon svg { width: 11px; height: 11px; }
  .contact__address { margin-top: 2px; line-height: 1.3; padding-right: 26px; }
</style>
</head>
<body>
<main class="canvas">
  <section class="card card--front" aria-label="Card front">
    <div class="brand">
      <span class="brand__mark"></span>
      <p class="brand__name">Ironvale<br>Protection Group</p>
    </div>
  </section>

  <section class="card card--back" aria-label="Card back">
    <div class="brand">
      <span class="brand__mark"></span>
      <p class="brand__name">Ironvale<br>Protection Group</p>
    </div>

    <div class="holder">
      <h1 class="holder__name">Marcus Ellery</h1>
      <p class="holder__title">Managing Director</p>
    </div>

    <div class="divider"></div>

    <ul class="contact">
      <li class="contact__item">044-555-0182
        <span class="contact__icon"><svg viewBox="0 0 12 12"><path d="M1 4c0-2 2-3 5-3s5 1 5 3l-2 1-1-2H4L3 5zM3 6h6l1 5H2z" fill="#f3c66a"/></svg></span></li>
      <li class="contact__item">123-555-0147
        <span class="contact__icon"><svg viewBox="0 0 12 12"><rect x="3" y="0.5" width="6" height="11" rx="1" fill="#f3c66a"/><rect x="4" y="2" width="4" height="7" fill="#6a1212"/></svg></span></li>
      <li class="contact__item">hello@ironvalepg.com
        <span class="contact__icon"><svg viewBox="0 0 12 12"><rect x="0.5" y="2" width="11" height="8" fill="#f3c66a"/><path d="M0.5 2L6 7l5.5-5" stroke="#6a1212" fill="none"/></svg></span></li>
      <li class="contact__item">www.ironvalepg.com
        <span class="contact__icon"><svg viewBox="0 0 12 12"><path d="M5 7l2-2M4 6L2.5 7.5a2 2 0 003 3L7 9M8 6l1.5-1.5a2 2 0 00-3-3L5 3" stroke="#f3c66a" stroke-width="1.5" fill="none"/></svg></span></li>
      <li class="contact__address">4820 Harbor Crest Lane<br>Westbridge, 204417.</li>
    </ul>
  </section>
</main>
</body>
</html>
```